Need Business Cards for my Business

email address: rkpmarlowhollowworks@vendrimail.com
web address: rkpmarlowhollowworks.net
Slogan: We offer various QVN licenses
Rowland K. Pemberly
Please stick with colors of Company Logo
would like the card to be more of the color example of the logo.
If you need PDF copy of logo email me at the above account.
Creative control rests with you.

Industry/Entity Type

Business

Contact Information for Business Card

I am a minimalist, but would like something to pop and stand out amongst other cards, make it memorable.

Font styles to use
Serif
Decorative
Script

```html
<!DOCTYPE html>
<html lang="en">
<head>
<meta charset="utf-8">
<title>Marlow Hollow Works – Business Cards</title>
<link href="https://fonts.googleapis.com/css2?family=Exo+2:wght@500;600&family=Raleway:wght@300;500;700&display=swap" rel="stylesheet">
<style>
  :root {
    --canvas: #e9e9ec;
    --ink-black: #05070c;
    --ink-navy: #1c2d4a;
    --glow-blue: #3a5a8c;
    --brand-blue: #1f5fae;
    --brand-red: #e53a40;
    --paper: #ffffff;
    --swoosh: #2a2f38;
    --text-light: #f2f4f8;
    --text-muted: #8ea0bf;
  }
  * { box-sizing: border-box; margin: 0; padding: 0; }
  html, body { width: 1200px; height: 913px; overflow: hidden; }
  body {
    background: var(--canvas);
    font-family: "Raleway", sans-serif;
    display: flex;
    align-items: center;
    justify-content: center;
    gap: 40px;
  }
  .card {
    position: relative;
    width: 540px;
    height: 309px;
    border-radius: 4px;
    overflow: hidden;
    box-shadow: 0 10px 28px rgba(0,0,0,.25);
  }
  .card--front {
    background: radial-gradient(ellipse 48% 52% at 50% 45%, var(--glow-blue) 0%, var(--ink-navy) 45%, var(--ink-black) 100%);
    display: flex;
    align-items: center;
    justify-content: center;
  }
  .brand-name {
    font-family: "Exo 2", sans-serif;
    font-weight: 600;
    letter-spacing: .14em;
    text-transform: uppercase;
    display: flex;
    align-items: center;
    gap: 12px;
  }
  .brand-name--front { color: var(--text-light); font-size: 26px; }
  .brand-mark {
    width: 14px; height: 14px;
    border-radius: 50%;
    background: var(--brand-red);
    flex: none;
  }
  .card--back {
    background: radial-gradient(ellipse 50% 60% at 30% 45%, var(--ink-navy) 0%, #0c1424 50%, var(--ink-black) 100%);
  }
  .back-panel { position: absolute; inset: 0; }
  .brand-name--back {
    position: absolute;
    right: 26px;
    top: 110px;
    color: var(--brand-blue);
    font-size: 15px;
    width: 150px;
    line-height: 1.3;
  }
  .brand-name--back .brand-mark { width: 12px; height: 12px; }
  .slogan {
    position: absolute;
    left: 150px;
    top: 88px;
    color: var(--text-muted);
    text-transform: uppercase;
    font-size: 16px;
    line-height: 1.05;
    text-align: center;
  }
  .slogan span { display: block; border-bottom: 1px solid var(--text-muted); }
  .slogan .slogan-light { font-weight: 300; }
  .slogan .slogan-bold { font-weight: 700; border-bottom: none; }
  .contact {
    position: absolute;
    left: 34px;
    bottom: 40px;
    color: var(--text-light);
  }
  .contact-name { font-weight: 700; font-size: 24px; margin-bottom: 8px; }
  .contact-line {
    display: flex; align-items: center; gap: 8px;
    font-weight: 300; font-size: 13.5px; margin-top: 5px;
  }
  .contact-line svg { width: 14px; height: 14px; flex: none; }
</style>
</head>
<body>

  <section class="card card--front" aria-label="Business card front">
    <div class="brand-name brand-name--front"><span class="brand-mark"></span>Marlow Hollow Works</div>
  </section>

  <section class="card card--back" aria-label="Business card back">
    <svg class="back-panel" viewBox="0 0 540 309" preserveAspectRatio="none" aria-hidden="true">
      <path d="M300 0 C330 110 400 230 540 262 L540 309 L540 0 Z" fill="var(--swoosh)"/>
      <path d="M318 0 C345 105 415 215 540 240 L540 0 Z" fill="var(--paper)"/>
    </svg>

    <div class="brand-name brand-name--back"><span class="brand-mark"></span>Marlow Hollow Works</div>

    <p class="slogan">
      <span class="slogan-bold" style="border-bottom:1px solid var(--text-muted)">We offer</span>
      <span class="slogan-light">Various QVN</span>
      <span class="slogan-bold">Licenses</span>
    </p>

    <div class="contact">
      <p class="contact-name">Rowland K. Pemberly</p>
      <p class="contact-line">
        <svg viewBox="0 0 16 16"><rect x="1" y="3" width="14" height="10" fill="none" stroke="#8ea0bf" stroke-width="1.2"/><path d="M1 3 L8 9 L15 3" fill="none" stroke="#8ea0bf" stroke-width="1.2"/></svg>
        rkpmarlowhollowworks@vendrimail.com
      </p>
      <p class="contact-line">
        <svg viewBox="0 0 16 16"><circle cx="8" cy="8" r="6.5" fill="none" stroke="#8ea0bf" stroke-width="1.2"/><ellipse cx="8" cy="8" rx="2.8" ry="6.5" fill="none" stroke="#8ea0bf" stroke-width="1"/><line x1="1.5" y1="8" x2="14.5" y2="8" stroke="#8ea0bf" stroke-width="1"/></svg>
        rkpmarlowhollowworks.net
      </p>
    </div>
  </section>

</body>
</html>
```